Killer design for artists website and gallery

Current website is www.bluemoorstudio.com.au and it runs on a very simple Wordpress standard theme. We would like a theme designed and customised to suit the branding and style. We have someone who will then code the site in HTML and CSS into Wordpress.

The general theme and branding can be seen on the site at the moment. Please note I have now uploaded full size files into the project. The website background files are for reference only as they are currently on the site. There is no requirement to use them in the new design, however the logo must be as per the attachment.. Please submit a home page/main gallery, and we will request additional pages (about us, other galleries etc.) from those designers we like during the project time.
Updates

Please note I have now uploaded full size files into the project. The website background files are for reference only as they are currently on the site. There is no requirement to use them in the new design, however the logo must be as per the attachment.

Target Market(s)

sales are only in Australia, and priced between approx $100 and $1000. Most viewers and buyers are 20-40 years old, and looking for a casual canvas work for home, or a gift.

Industry/Entity Type

Artists

Font styles to use
Serif
Sans Serif

Requirements
Must have
• gallery of images, responsive design, ability to select categories of pictures (see top menu on current site) and have the gallery change to match, colours to match branding and logo.
Nice to have
• simple minimalist style is preferred. More like http://www.tobiasmerrow.com/ than http://www.harbourpaintco.com.au/ or http://www.velvetcanvas.com.au/
Should not have
• does not need any online store, or shopping cart etc.

```html
<!DOCTYPE html>
<html lang="en">
<head>
<meta charset="utf-8">
<title>Bluemoor Studio – Canvas art made in Melbourne</title>
<link href="https://fonts.googleapis.com/css2?family=Noto+Sans:wght@400;700&display=swap" rel="stylesheet">
<style>
  :root {
    --page-bg: #d4d4d4;
    --sidebar-bg: #2a2a2a;
    --panel-bg: #e6e6e6;
    --panel-edge: #dcdcdc;
    --logo-bg: #120e0e;
    --accent: #e8e100;
    --nav-text: #dddddd;
    --ink: #2b2b2b;
    --bar: #2b2b2b;
    --slide-top: #3b6fc0;
    --slide-mid: #4a6fb8;
    --slide-low: #2e4f96;
  }
  * { box-sizing: border-box; margin: 0; padding: 0; }
  html, body { width: 1200px; height: 1000px; overflow: hidden; }
  body {
    position: relative;
    background: var(--page-bg);
    font-family: "Noto Sans", Verdana, sans-serif;
    color: var(--ink);
  }
  .sidebar {
    position: absolute; left: 115px; top: 0; width: 187px; height: 1000px;
    background: repeating-linear-gradient(135deg, #2e2e2e 0 2px, #262626 2px 4px);
  }
  .main-panel {
    position: absolute; left: 302px; top: 0; width: 785px; height: 1000px;
    background: var(--panel-bg);
    box-shadow: 4px 0 10px rgba(0,0,0,0.12);
  }
  .content-sheet {
    position: absolute; left: 400px; top: 70px; width: 602px; height: 930px;
    background: var(--panel-bg);
    box-shadow: 3px 0 8px rgba(0,0,0,0.10);
  }
  .logo {
    position: absolute; left: 137px; top: 60px; width: 191px; height: 190px;
    background: var(--logo-bg);
    border: 1.5px solid var(--accent);
    border-radius: 14px;
    display: flex; flex-direction: column; justify-content: flex-end;
    padding: 0 0 18px 14px;
    color: #ffffff;
  }
  .logo-name { font-size: 24px; font-weight: 400; line-height: 1.1; letter-spacing: 0.5px; }
  .main-nav { position: absolute; left: 137px; top: 311px; list-style: none; }
  .main-nav li {
    height: 39.7px; font-size: 17px; text-transform: uppercase; color: var(--nav-text);
  }
  .main-nav li.is-current { color: var(--accent); }
  .social-links { position: absolute; left: 115px; top: 854px; }
  .social-links svg { display: block; margin-bottom: 10px; }
  .tagline { position: absolute; left: 416px; top: 84px; width: 570px; height: 160px; }
  .tagline span { position: absolute; white-space: nowrap; color: var(--ink); }
  .tag-small { font-size: 25px; font-weight: 400; }
  .tag-big { font-size: 57px; font-weight: 700; line-height: 1; }
  .slider { position: absolute; left: 415px; top: 313px; width: 568px; }
  .slide {
    height: 360px;
    background: linear-gradient(180deg, var(--slide-top) 0%, var(--slide-mid) 55%, var(--slide-low) 100%);
  }
  .slider-bar {
    height: 45px; background: var(--bar);
    display: flex; align-items: center; gap: 10px; padding-left: 30px;
    box-shadow: 0 6px 10px rgba(0,0,0,0.18);
  }
  .slider-dot { width: 10px; height: 10px; background: #ffffff; }
  .slider-dot.is-active { background: var(--accent); }
  .intro { position: absolute; left: 427px; top: 787px; width: 555px; }
  .intro h2 { font-size: 25px; font-weight: 700; margin-bottom: 10px; }
  .intro p { font-size: 18.5px; line-height: 24px; }
</style>
</head>
<body>
  <aside class="sidebar"></aside>
  <main class="main-panel"></main>
  <div class="content-sheet"></div>

  <div class="logo">
    <span class="logo-name">BLUEMOOR<br>STUDIO</span>
  </div>

  <ul class="main-nav">
    <li class="is-current">Home</li>
    <li>About</li>
    <li>Cityscapes</li>
    <li>Other Work</li>
    <li>Seascapes</li>
    <li>Testimonials</li>
    <li>Work for Sale</li>
  </ul>

  <div class="social-links">
    <svg width="52" height="25" viewBox="0 0 52 25"><polygon points="0,0 52,0 44,12.5 52,25 0,25" fill="#4a5f96"/></svg>
    <svg width="52" height="25" viewBox="0 0 52 25"><polygon points="0,0 52,0 44,12.5 52,25 0,25" fill="#c53a2c"/></svg>
    <svg width="52" height="25" viewBox="0 0 52 25"><polygon points="0,0 52,0 44,12.5 52,25 0,25" fill="#2fa0cf"/></svg>
  </div>

  <h1 class="tagline">
    <span class="tag-small" style="left:4px; top:0;">Beautiful</span>
    <span class="tag-big" style="left:0; top:30px;">canvas art</span>
    <span class="tag-small" style="left:94px; top:95px;">made in</span>
    <span class="tag-big" style="left:212px; top:94px;">Melbourne</span>
  </h1>

  <section class="slider">
    <div class="slide" role="img" aria-label="Acrylic triptych painting of a couple sharing an umbrella in blue dripping rain"></div>
    <div class="slider-bar">
      <span class="slider-dot is-active"></span>
      <span class="slider-dot"></span>
      <span class="slider-dot"></span>
    </div>
  </section>

  <section class="intro">
    <h2>Northbank Makers Market</h2>
    <p>Clara Moor is a local artist who paints with acrylics, specialising in seascapes, landscapes and cityscapes. She has painted for many years and studied under es­tablished artists in Melbourne.</p>
  </section>
</body>
</html>
```